Top Real Estate teams new cards UPDATED

New Cards with MY (Im the tall guy in the middle) new pic on the front of card and my team pic on the back of card. Also my team name on the front of the card (marlow and partners) and brokerage name on the back (harborline real estate group) . Also the tag line "Ask about our 20 step plan" on the back of the card and "Welcome to the new way of Real Estate Sales" on the front of the card along with my phone number (951-482-3067) and email address (derek.marlow47@quillmail.net) my website (www.DerekMarlow.org) and my License number (BRE:07315294). I do like my team name colors of black and gold
Logo links are attached:
1. https://www.filevaultly.net/sh/815kqwz73hpadrx/AAG7MmK2PlR4ZqWsYnUuE_HQb?dl=0
2. https://www.filevaultly.net/sh/29c7vxm84tq015r/AACKDRLW46NeT2Gh8Vr4Jk7Yb?dl=0
Updates

Target Market(s)

Real Estate Customers

Industry/Entity Type

Real Estate

Contact Information for Business Card

Classy, yet east ro read and understand

Font styles to use
Sans Serif

Requirements
Must have
• Team and brokerage name, and both slogans.
• Black and gold color scheme.
Nice to have
• Bold writing
Should not have
• cluttered feeling

```html
<!DOCTYPE html>
<html lang="en">
<head>
<meta charset="utf-8">
<title>Marlow and Partners – Business Cards</title>
<link rel="stylesheet" href="https://fonts.googleapis.com/css2?family=Cinzel:wght@400&family=Open+Sans:ital,wght@0,400;0,600;1,700&display=swap">
<style>
  :root {
    --page: #e4e4e4;
    --card: #ffffff;
    --ink: #231f20;
    --ink-soft: #4a4a4a;
    --gold: #c49a22;
    --rule: #cfcfcf;
  }
  * { margin: 0; padding: 0; box-sizing: border-box; }
  html, body { width: 1200px; height: 987px; overflow: hidden; }
  body {
    background: var(--page);
    font-family: "Open Sans", Arial, sans-serif;
    color: var(--ink);
    position: relative;
  }
  .card {
    position: absolute;
    left: 293px;
    width: 615px;
    height: 352px;
    background: var(--card);
    box-shadow: 0 2px 6px rgba(0,0,0,0.18);
    overflow: hidden;
  }
  .card--front { top: 130px; }
  .card--back { top: 505px; }

  .brand {
    position: absolute;
    display: flex;
    flex-direction: column;
    align-items: center;
    text-align: center;
  }
  .brand__mark {
    width: 64px; height: 64px;
    border-radius: 50%;
    background: var(--ink);
  }
  .brand__name {
    font-family: "Cinzel", Georgia, serif;
    font-weight: 400;
    color: var(--ink);
    font-size: 35px;
    line-height: 32px;
    margin-top: 12px;
  }
  .card--front .brand { left: 20px; top: 100px; width: 280px; }
  .card--back .brand { left: 4px; top: 164px; width: 280px; }
  .card--back .brand__name { font-size: 33px; line-height: 31px; }

  .divider {
    position: absolute;
    left: 307px; top: 89px;
    width: 1px; height: 162px;
    background: var(--rule);
  }
  .contact { position: absolute; left: 335px; top: 90px; }
  .contact__name { font-size: 22px; font-weight: 600; line-height: 28px; }
  .contact__role { font-size: 17px; color: var(--gold); line-height: 22px; }
  .contact__licence { font-size: 15px; color: var(--ink-soft); margin-top: 8px; line-height: 20px; }
  .contact__list { list-style: none; margin-top: 8px; }
  .contact__item {
    display: flex; align-items: center; gap: 7px;
    font-size: 16px; color: var(--ink-soft); line-height: 24px;
  }
  .contact__item svg { width: 14px; height: 14px; fill: var(--ink); flex: none; }

  .band { position: absolute; left: 0; bottom: 0; width: 615px; height: 36px; }
  .band svg { position: absolute; inset: 0; }
  .band__text {
    position: absolute; left: 35px; top: 0;
    line-height: 36px; font-size: 16px; color: #fff;
  }

  .brokerage {
    position: absolute; left: 39px; top: 34px;
    font-size: 11px; font-weight: 400; color: var(--ink);
    letter-spacing: 0.5px;
  }
  .tagline {
    position: absolute; left: 41px; top: 300px;
    font-size: 16px; font-weight: 700; font-style: italic; color: var(--gold);
  }
  .portrait {
    position: absolute; left: 340px; top: 16px;
    width: 275px; height: 336px;
    background: linear-gradient(180deg, #f3ece6 0%, #c99f84 35%, #3a2f2c 70%, #151313 100%);
  }
</style>
</head>
<body>
  <section class="card card--front">
    <div class="brand">
      <div class="brand__mark"></div>
      <div class="brand__name">Marlow and<br>Partners</div>
    </div>
    <div class="divider"></div>
    <div class="contact">
      <div class="contact__name">Derek Marlow</div>
      <div class="contact__role">Owner</div>
      <div class="contact__licence">BRE: 07315294</div>
      <ul class="contact__list">
        <li class="contact__item">
          <svg viewBox="0 0 24 24"><path d="M6.6 10.8a15.1 15.1 0 0 0 6.6 6.6l2.2-2.2c.3-.3.7-.4 1-.2 1.1.4 2.3.6 3.6.6.6 0 1 .4 1 1V20c0 .6-.4 1-1 1A17 17 0 0 1 3 4c0-.6.4-1 1-1h3.5c.6 0 1 .4 1 1 0 1.3.2 2.5.6 3.6.1.3 0 .7-.2 1z"/></svg>
          (951-482-3067)
        </li>
        <li class="contact__item">
          <svg viewBox="0 0 24 24"><path d="M2 5h20v14H2z M2 5l10 8 10-8" fill="none" stroke="#231f20" stroke-width="2"/><path d="M2 5h20l-10 8z"/></svg>
          derek.marlow47@quillmail.net
        </li>
        <li class="contact__item">
          <svg viewBox="0 0 24 24"><circle cx="12" cy="12" r="10"/><path d="M2 12h20M12 2c3 3 3 17 0 20M12 2c-3 3-3 17 0 20" fill="none" stroke="#fff" stroke-width="1.5"/></svg>
          www.DerekMarlow.org
        </li>
      </ul>
    </div>
    <div class="band">
      <svg width="615" height="36" viewBox="0 0 615 36">
        <polygon points="0,0 408,0 398,36 0,36" fill="#231f20"/>
        <polygon points="414,0 615,0 615,36 404,36" fill="#c49a22"/>
      </svg>
      <span class="band__text">Welcome to the new way of Real Estate Sales</span>
    </div>
  </section>

  <section class="card card--back">
    <div class="brokerage">Harborline Real Estate Group</div>
    <div class="brand">
      <div class="brand__mark"></div>
      <div class="brand__name">Marlow and<br>Partners</div>
    </div>
    <div class="tagline">Ask about our 20 step plan</div>
    <div class="portrait" role="img" aria-label="Portrait photo of the agent in a dark suit and tie"></div>
  </section>
</body>
</html>
```